Looking to design a new sign for our church.

Looking for a new sign
4 x 8 feet dimension
We are renaming the church "Medlow Ridge Community Church"
looking for legible graphics
Would like some type of backdrop being a family tree (oak) / open to other ideas as you are led
I have included a pic of the old sign for your review
would like to incorporate our ministry logo on the lower right hand corner of the sign / see file attached

```html
<!DOCTYPE html>
<html lang="en">
<head>
<meta charset="utf-8">
<title>Medlow Ridge Community Church — Sign</title>
<link href="https://fonts.googleapis.com/css2?family=Cinzel:wght@400&family=Montserrat:wght@600&display=swap" rel="stylesheet">
<style>
  :root {
    --backdrop: #c9c9c9;
    --navy: #001638;
    --navy-light: #001b45;
    --gold-dark: #9a7e42;
    --gold-light: #e8cf86;
    --white: #ffffff;
    --divider: #3f5d70;
  }
  html, body {
    margin: 0;
    width: 1200px;
    height: 1200px;
    overflow: hidden;
    background: var(--backdrop);
  }
  .sign {
    position: absolute;
    left: 40px;
    top: 288px;
    width: 1078px;
    height: 580px;
    box-sizing: border-box;
    background: linear-gradient(90deg, var(--gold-dark), var(--gold-light) 50%, var(--gold-dark));
    padding: 9px;
  }
  .sign-panel {
    position: relative;
    width: 100%;
    height: 100%;
    background: linear-gradient(120deg, var(--navy) 40%, var(--navy-light));
  }
  .sign-frame {
    position: absolute;
    left: 9px;
    top: 11px;
    width: 1042px;
    height: 534px;
    overflow: visible;
  }
  .church-name {
    position: absolute;
    left: 0;
    width: 100%;
    margin: 0;
    text-align: center;
    font-family: "Cinzel", "Times New Roman", serif;
    font-weight: 400;
    color: var(--white);
    line-height: 1;
    white-space: nowrap;
  }
  .church-name--first { top: 280px; font-size: 66px; letter-spacing: 2px; }
  .church-name--second { top: 348px; font-size: 52px; letter-spacing: 3px; }
  .schedule {
    position: absolute;
    top: 464px;
    font-family: "Montserrat", Arial, sans-serif;
    font-weight: 600;
    font-size: 24px;
    line-height: 29px;
    color: var(--white);
    margin: 0;
    padding: 0;
    list-style: none;
  }
  .schedule--times { left: 271px; }
  .schedule--events { left: 519px; }
  .schedule-divider {
    position: absolute;
    left: 455px;
    top: 464px;
    width: 1px;
    height: 82px;
    background: var(--divider);
  }
</style>
</head>
<body>
  <div class="sign">
    <div class="sign-panel">
      <svg class="sign-frame" width="1042" height="534" viewBox="0 0 1042 534">
        <defs>
          <linearGradient id="gold" x1="0" y1="0" x2="1" y2="1">
            <stop offset="0" stop-color="#9a7e42"/>
            <stop offset="0.5" stop-color="#e8cf86"/>
            <stop offset="1" stop-color="#9a7e42"/>
          </linearGradient>
        </defs>
        <polyline points="218,532 2,532 2,2 1040,2 1040,532 847,532" fill="none" stroke="url(#gold)" stroke-width="4"/>
        <circle cx="528" cy="147" r="101" fill="none" stroke="url(#gold)" stroke-width="6"/>
      </svg>

      <h1 class="church-name church-name--first">MEDLOW RIDGE</h1>
      <p class="church-name church-name--second">COMMUNITY CHURCH</p>

      <ul class="schedule schedule--times">
        <li>10:30 AM</li>
        <li>9:30 AM</li>
        <li>6:00 PM</li>
      </ul>
      <div class="schedule-divider"></div>
      <ul class="schedule schedule--events">
        <li>WORSHIP SERVICE</li>
        <li>SUNDAY SCHOOL</li>
        <li>WEDNESDAY SERVICE</li>
      </ul>
    </div>
  </div>
</body>
</html>
```